Business Card Design

Lintel Comms is a public relations consultancy service for the self build, home refurbishment and home improvement market.
It represents everything about 'home' so envisage logo featuring maybe roof pitch over the 'A' of Lintel. Colour/font undecided.

Industry/Entity Type

Home Improvement

Contact Information for Business Card

Fenella Coxworth
fenella@lintelcomms.co.uk
Telephone Direct: 0788 142 6597

```html
<!DOCTYPE html>
<html lang="en">
<head>
<meta charset="utf-8">
<title>Lintel Comms – Business Card</title>
<link rel="stylesheet" href="https://fonts.googleapis.com/css2?family=Sarabun:wght@300;400;500&display=swap">
<style>
  :root {
    --slate: #5a6a6a;
    --slate-text: #55676a;
    --paper: #fdfdfd;
    --frame: #ffffff;
  }
  html, body {
    margin: 0;
    padding: 0;
    width: 1200px;
    height: 791px;
    overflow: hidden;
    background: var(--slate);
  }
  .card {
    position: relative;
    width: 1200px;
    height: 791px;
    background: var(--slate);
    font-family: "Sarabun", Arial, sans-serif;
    overflow: hidden;
  }
  .card__shapes {
    position: absolute;
    inset: 0;
  }
  .brand {
    position: absolute;
    left: 0;
    top: 322px;
    width: 1180px;
    margin: 0;
    text-align: center;
    color: #ffffff;
    font-size: 86px;
    font-weight: 500;
    letter-spacing: 0.09em;
    line-height: 1;
    white-space: nowrap;
  }
  .contact {
    position: absolute;
    left: 450px;
    top: 552px;
    color: var(--slate-text);
  }
  .contact__name {
    margin: 0;
    font-size: 58px;
    font-weight: 400;
    letter-spacing: 0.03em;
    line-height: 1;
    text-transform: uppercase;
  }
  .contact__line {
    margin: 0;
    font-size: 30px;
    font-weight: 400;
    line-height: 1;
  }
  .contact__email { margin-top: 14px; }
  .contact__phone { margin-top: 20px; letter-spacing: 0.02em; }
</style>
</head>
<body>
  <main class="card">
    <svg class="card__shapes" width="1200" height="791" viewBox="0 0 1200 791" aria-hidden="true">
      <rect class="frame" x="35" y="88" width="1131" height="614" fill="none" stroke="var(--frame)" stroke-width="2"/>
      <polygon class="contact-panel" points="381,500 1200,500 1200,791 0,791 0,786" fill="var(--paper)"/>
    </svg>

    <h1 class="brand">LINTEL COMMS</h1>

    <section class="contact">
      <p class="contact__name">Fenella&nbsp; Coxworth</p>
      <p class="contact__line contact__email">fenella@lintelcomms.co.uk</p>
      <p class="contact__line contact__phone">Telephone Direct: 0788 142 6597</p>
    </section>
  </main>
</body>
</html>
```